Brookvane Estates LLC stationary for a real estate property management company.

Create stationary (letterhead, envelopes, business cards) using Brookvane Estates LLC logo as primary creative element. Stationary design needs to be horizontal, leaving as much space as possible for correspondence copy. See attached Creative Brief and past stationary files for details.

Target Market(s)

Prospective apartment residents and current residents, vendors, and government agencies.

Industry/Entity Type

Property Management

Contact Information for Business Card

Business card employee title: Property Manager. Should include address, phone, fax, email, website, slogan, and Brookvane Estates logo.

Font styles to use
Sans Serif

Colors
0592cd
000000

Requirements
Must have
• Tone should be conservative, institutional, business (i.e. banking, finance, real estate). Must include: address, phone, fax, website, and slogan (see attached Creative Brief). Should be a horizontal design, leaving as much room as possible for letter correspondence copy.
Nice to have
• Please use an Arial or Helvetica style font.
Should not have
• Letterhead layout should leave as much room as possible for copy.

```html
<!DOCTYPE html>
<html lang="en">
<head>
<meta charset="utf-8">
<title>Brookvane Estates LLC Stationery</title>
<link href="https://fonts.googleapis.com/css2?family=Arimo:wght@400;700&display=swap" rel="stylesheet">
<style>
:root{
  --blue:#0a6aa9;
  --blue-soft:#3b87bd;
  --charcoal:#444549;
  --paper:#f3f3f3;
  --ink:#222;
  --backdrop:#cfcdd0;
  --faint:#e2e2e6;
}
*{box-sizing:border-box;margin:0;padding:0}
html,body{width:1189px;height:1200px;overflow:hidden}
body{background:var(--backdrop);font-family:"Arimo",Arial,sans-serif;color:var(--ink);position:relative}
.item{position:absolute;overflow:hidden}
.wordmark{display:flex;align-items:center;gap:6px;font-weight:700;color:var(--blue);white-space:nowrap}
.wordmark .mark{background:currentColor;flex:none}
.wordmark.light{color:#fff}
.deco-ring{position:absolute;border-radius:50%;border-style:solid}
.topbar{position:absolute;top:0;left:0;right:0;height:10px;display:flex}
.topbar .b{flex:0 0 67%;background:var(--blue)}
.topbar .g{flex:1;background:var(--charcoal);margin-left:3px}

/* folder */
.folder{left:112px;top:78px;width:424px;height:551px;background:var(--blue)}
.folder .wordmark{position:absolute;left:50px;top:124px;font-size:26px;gap:10px}
.folder .wordmark .mark{width:26px;height:26px}
.folder .deco-ring{left:108px;top:210px;width:440px;height:440px;border-width:14px;border-color:var(--blue-soft)}
.folder .url{position:absolute;left:107px;top:500px;color:#fff;font-size:16px}

/* letterhead */
.letterhead{left:640px;top:85px;width:422px;height:544px;background:var(--paper)}
.letterhead .wordmark{position:absolute;left:42px;top:42px;font-size:15px}
.letterhead .wordmark .mark{width:14px;height:14px}
.contact{position:absolute;left:302px;top:26px;font-size:6.3px;line-height:7.4px;border-left:1px solid var(--ink);padding-left:4px}
.contact .gap{height:6px}
.letterhead .deco-ring{left:255px;top:375px;width:230px;height:230px;border-width:8px;border-color:var(--faint)}
.letter{position:absolute;left:41px;top:140px;width:345px;font-size:7px;line-height:12px;text-align:justify}
.letter p{margin-bottom:12px}
.signature{position:absolute;left:41px;top:405px;width:120px;height:32px;background:linear-gradient(90deg,#d9d9d9,#ececec);border-radius:3px}
.sig-title{position:absolute;left:41px;top:444px;font-size:7.5px}

/* envelope front */
.env-front{left:112px;top:677px;width:371px;height:184px;background:var(--paper)}
.env-front .wordmark{position:absolute;left:16px;top:24px;font-size:10px;gap:4px}
.env-front .wordmark .mark{width:9px;height:9px}
.env-front .addr{position:absolute;left:18px;top:48px;font-size:5.5px;line-height:7px}
.env-front .deco-ring{left:262px;top:48px;width:170px;height:170px;border-width:6px;border-color:var(--faint)}

/* envelope back */
.env-back{left:112px;top:918px;width:371px;height:184px;background:var(--paper)}
.env-back svg{position:absolute;left:0;top:0}
.env-back .seal{position:absolute;left:179px;top:30px;width:14px;height:14px;background:#fff;border-radius:50%}

/* business card front */
.card-front{left:524px;top:763px;width:269px;height:157px;background:var(--paper)}
.card-front .topbar{height:6px}
.card-front .wordmark{position:absolute;left:15px;top:27px;font-size:11px;gap:4px}
.card-front .wordmark .mark{width:10px;height:10px}
.card-front .deco-ring{left:160px;top:45px;width:150px;height:150px;border-width:6px;border-color:var(--faint)}
.person{position:absolute;left:18px;top:62px;font-size:7.5px;line-height:9px}
.person strong{color:var(--blue)}
.card-lines{position:absolute;left:18px;top:89px;font-size:6.5px;line-height:8.3px}
.card-lines .row{display:flex;align-items:center;gap:4px}
.card-lines svg{flex:none}
.card-addr{position:absolute;left:18px;top:131px;font-size:6.5px}

/* business card back */
.card-back{left:526px;top:947px;width:268px;height:153px;background:var(--blue)}
.card-back .deco-ring{left:122px;top:-8px;width:200px;height:200px;border-width:8px;border-color:var(--blue-soft)}
.card-back .wordmark{position:absolute;left:20px;top:117px;font-size:11px;gap:4px}
.card-back .wordmark .mark{width:10px;height:10px}

/* notebook */
.notebook{left:863px;top:823px;width:202px;height:277px;background:var(--blue);overflow:visible}
.notebook .deco-ring{left:48px;top:115px;width:210px;height:210px;border-width:10px;border-color:var(--blue-soft);clip-path:inset(0 56px 50px 0)}
.notebook .wordmark{position:absolute;left:45px;top:42px;font-size:11px;gap:4px}
.notebook .wordmark .mark{width:10px;height:10px}
.spiral{position:absolute;left:-6px;top:14px;width:6px;height:250px;background:repeating-linear-gradient(180deg,#9a9a9e 0 2px,transparent 2px 8px)}

/* erasers */
.eraser{top:675px;height:51px;border-radius:3px}
.eraser.white{left:758px;width:130px;background:#f1f1f1}
.eraser.white .cap{position:absolute;right:0;top:0;width:24px;height:100%;background:#2a2a2a}
.eraser.blue{left:921px;width:133px;background:var(--blue)}
.eraser.blue .cap{position:absolute;right:0;top:0;width:24px;height:100%;background:#f1f1f1}
.eraser .wordmark{position:absolute;left:12px;top:20px;font-size:8px;gap:3px}
.eraser .wordmark .mark{width:8px;height:8px}
</style>
</head>
<body>

<section class="item folder" aria-label="Presentation folder">
  <div class="deco-ring"></div>
  <div class="wordmark light"><span class="mark"></span>Brookvane Estates LLC</div>
  <div class="url">www.brookvaneestates.com</div>
</section>

<section class="item letterhead" aria-label="Letterhead">
  <div class="topbar"><span class="b"></span><span class="g"></span></div>
  <div class="wordmark"><span class="mark"></span>Brookvane Estates LLC</div>
  <div class="contact">
    <div>555-310-4827</div><div>555-310-4828</div>
    <div>nora@brookvaneestates.com</div><div>www.brookvaneestates.com</div>
    <div class="gap"></div>
    <div>2180 Alder Row #204</div><div>Fairhaven, CA 90210</div>
  </div>
  <div class="deco-ring"></div>
  <div class="letter">
    <p>Dear Client</p>
    <p>Lorem ipsum dolor sit amet, consectetur adipiscing elit. Pellentesque semper purus ornare dolor eleifend aliquam. Integer molestie gravida sem a porttitor. Quisque pulvinar tellus ut ipsum molestie ultricies id non turpis. Phasellus feugiat ornare feugiat. Integer nec velit eu justo laoreet condimentum. Aenean non commodo quam. Phasellus lacinia aliquet turpis. Praesent non elit nec ante porta cursus.</p>
    <p>Curabitur nec venenatis risus. Integer nec nisi sit amet leo mattis aliquam. Vivamus vulputate tellus quis purus lobortis rutrum. Aenean nec ipsum ut mauris faucibus facilisis vel porttitor neque. Morbi molestie magna id neque scelerisque ut iaculis justo porttitor. Sed est ligula, semper at cursus ac, porttitor ac ipsum. Maecenas pulvinar euismod tempor.</p>
    <p>Maecenas vel neque ante, id faucibus ipsum. Suspendisse non neque quis nunc rhoncus bibendum. Fusce sit amet quam quis libero facilisis ultrices. Donec dignissim lorem vel sem sodales mollis. Duis nec sem lorem, at tristique nibh. In rutrum fermentum lectus, nec dictum leo tincidunt in.</p>
  </div>
  <div class="signature" role="img" aria-label="Handwritten signature"></div>
  <div class="sig-title">Managing Director</div>
</section>

<section class="item env-front" aria-label="Envelope front">
  <div class="topbar" style="height:7px"><span class="b"></span><span class="g"></span></div>
  <div class="deco-ring"></div>
  <div class="wordmark"><span class="mark"></span>Brookvane Estates LLC</div>
  <div class="addr">2180 Alder Row #204 Fairhaven,<br>CA 90210</div>
</section>

<section class="item env-back" aria-label="Envelope back">
  <svg width="371" height="184" viewBox="0 0 371 184">
    <path d="M0 0 H371 L362 52 Q360 60 352 60 H20 Q11 60 9 52 Z" fill="var(--blue)"/>
  </svg>
  <div class="seal"></div>
</section>

<section class="item card-front" aria-label="Business card front">
  <div class="topbar"><span class="b"></span><span class="g"></span></div>
  <div class="deco-ring"></div>
  <div class="wordmark"><span class="mark"></span>Brookvane Estates LLC</div>
  <div class="person"><strong>NORA WHITFIELD</strong><br>Property Manager</div>
  <div class="card-lines">
    <div class="row"><svg width="6" height="6" viewBox="0 0 6 6"><rect width="6" height="6" rx="1" fill="var(--blue)"/></svg>555-310-4827</div>
    <div class="row"><svg width="6" height="6" viewBox="0 0 6 6"><rect width="6" height="6" fill="var(--blue)"/></svg>555-310-4828</div>
    <div class="row"><svg width="6" height="6" viewBox="0 0 6 6"><rect y="1" width="6" height="4" fill="var(--blue)"/></svg>nora@brookvaneestates.com</div>
    <div class="row"><svg width="6" height="6" viewBox="0 0 6 6"><circle cx="3" cy="3" r="3" fill="#8aa0b8"/></svg>www.brookvaneestates.com</div>
  </div>
  <div class="card-addr">2180 Alder Row #204 Fairhaven, CA 90210</div>
</section>

<section class="item card-back" aria-label="Business card back">
  <div class="deco-ring"></div>
  <div class="wordmark light"><span class="mark"></span>Brookvane Estates LLC</div>
</section>

<section class="item notebook" aria-label="Notebook cover">
  <div class="spiral"></div>
  <div class="deco-ring"></div>
  <div class="wordmark light"><span class="mark"></span>Brookvane Estates LLC</div>
</section>

<section class="item eraser white" aria-label="Branded eraser">
  <div class="wordmark"><span class="mark"></span>Brookvane Estates</div>
  <div class="cap"></div>
</section>
<section class="item eraser blue" aria-label="Branded eraser">
  <div class="wordmark light"><span class="mark"></span>Brookvane Estates</div>
  <div class="cap"></div>
</section>

</body>
</html>
```